We need a book cover designed for a book that our CEO just finished writing. His name is Dale Voskin. So it'll need to have his name on it as the author. The title of the book is "88 Simple Moves to Expand Your Training Space." It needs to relate to fitness studio owners/gym owners as they're the target audience. What will this pricing look like?

Target Market(s)

Fitness studio owners and gym owners

Industry/Entity Type

Fitness

Font styles to use
Other font styles liked:
• The font we usually use for our brand is bebas neue. Not saying that needs to be done here, but we'd love to see it as one of the 3 options.

Colors

Designer to choose colors to be used in the design.

Requirements
Must have
• The title and author as Dale Voskin
Should not have
• Clutter!

```html
<!DOCTYPE html>
<html lang="en">
<head>
<meta charset="utf-8">
<title>88 Simple Moves to Expand Your Training Space — Dale Voskin</title>
<link rel="stylesheet" href="https://fonts.googleapis.com/css2?family=Bebas+Neue&family=Montserrat:wght@600&display=swap">
<style>
  :root {
    --ink: #121212;
    --white: #ffffff;
    --lime-top: #a3c531;
    --lime-bottom: #d6e85e;
    --lime-bright: #c8de3c;
    --lime-deep: #86a63a;
    --lime-flat: #b4d23a;
    --photo-light: #5a5a5a;
    --photo-mid: #2e2e2e;
  }
  * { margin: 0; padding: 0; box-sizing: border-box; }
  html, body {
    width: 800px; height: 1200px; overflow: hidden;
    background: var(--ink);
  }
  .cover {
    position: relative; width: 800px; height: 1200px;
    background: var(--ink); overflow: hidden;
  }
  .author {
    position: absolute; left: 206px; top: 52px;
    width: 384px; height: 54px;
    border: 2px solid var(--white);
    display: flex; align-items: center; justify-content: center;
    font-family: "Montserrat", sans-serif; font-weight: 600;
    font-size: 34px; letter-spacing: 0.3em; color: var(--white);
    padding-left: 0.3em; white-space: nowrap;
  }
  .author-portrait {
    position: absolute; left: 8px; top: 120px;
    width: 784px; height: 560px;
    background: radial-gradient(ellipse 45% 60% at 50% 55%,
      var(--photo-light) 0%, var(--photo-mid) 55%, var(--ink) 100%);
  }
  .title {
    position: absolute; left: 0; top: 0; width: 800px; height: 1200px;
    font-family: "Bebas Neue", sans-serif; font-weight: 400;
    line-height: 1; color: var(--white);
  }
  .title-top {
    position: absolute; top: 584px; left: 0; width: 800px;
    display: flex; justify-content: center; align-items: flex-start; gap: 22px;
  }
  .title-number {
    font-size: 200px; line-height: 0.85;
    background: linear-gradient(180deg, var(--lime-top), var(--lime-bottom));
    -webkit-background-clip: text; background-clip: text; color: transparent;
  }
  .title-lines { display: flex; flex-direction: column; padding-top: 14px; }
  .title-kicker { font-size: 68px; line-height: 0.9; }
  .title-kicker .accent { color: var(--lime-flat); }
  .title-sub { font-size: 98px; line-height: 0.88; }
  .title-main {
    position: absolute; left: 0; width: 800px; text-align: center;
  }
  .title-main.white { top: 738px; font-size: 220px; line-height: 0.9; }
  .title-main.lime {
    top: 926px; font-size: 280px; line-height: 0.85;
  }
  .title-main.lime span {
    background: linear-gradient(180deg, var(--lime-bright), var(--lime-deep));
    -webkit-background-clip: text; background-clip: text; color: transparent;
  }
</style>
</head>
<body>
  <main class="cover">
    <div class="author-portrait" role="img" aria-label="Black and white photo of the author smiling with arms spread wide"></div>
    <div class="author">DALE VOSKIN</div>
    <h1 class="title">
      <div class="title-top">
        <span class="title-number">88</span>
        <span class="title-lines">
          <span class="title-kicker"><span class="accent">SIMPLE MOVES</span> TO</span>
          <span class="title-sub">EXPAND YOUR</span>
        </span>
      </div>
      <div class="title-main white">TRAINING</div>
      <div class="title-main lime"><span>SPACE</span></div>
    </h1>
  </main>
</body>
</html>
```